PACKAGING AND LABEL DESIGN FOR LUXURY WHISKY BRAND

We need a label and packaging design for a new luxury whisky brand based in Singapore called Velmo. We need a label design and a suggested packaging design in a box/bag or wrap form. For the bottle it is fixed, so we would like suggestions to make the bottle like a piece of art. Please refer to Harrow whisky, Tizzo Rum, PLK and Morvi coffee for the inspiration and styles we like. For the words 1764 and Reed Whisky please make original fonts or artwork. We would like it to be in Serif font but we are open to suggestions
The bottle is as attached with the following dimensions
Height :159mm
Diammeter:84mm
Outter Diameter of mouth:39mm

We develop the world's first soy wines and spirits. Our new product is a soy based whisky that pays tribute to tradition and culture in Singapore while showcasing our nation's innovative and courageous spirit, moving from a swamp to a first world nation.

Please read the brand guidelines for deeper understanding

Target Market(s)

Global travellers coming to Singapore. Adventurous, innovators and independent self made pride.

Industry/Entity Type

Alcohol beverages

Requirements
Must have
• Original label design a box/packaging design, logo of velmo, logo of 1764, fonts and art of the labels
Nice to have
• Original artwork for 1764 and Reed Whisky. Batik prints, gold, soy beans/flowers, Singapore elements.
Should not have
• No copied work.

```html
<!DOCTYPE html>
<html lang="en">
<head>
<meta charset="utf-8">
<title>Velmo 1764 Reed Whisky — Label and Palette</title>
<link rel="stylesheet" href="https://fonts.googleapis.com/css2?family=Josefin+Sans:wght@400&family=Questrial&family=Permanent+Marker&display=swap">
<style>
  :root {
    --forest: #13322B;
    --gold: #B38808;
    --mist: #E1E0DC;
    --board: #EEEEEE;
    --stage: #D6D6DB;
    --label-paper: #ECECEA;
    --ink-soft: #3B3B3B;
    --white: #FFFFFF;
  }
  * { box-sizing: border-box; margin: 0; padding: 0; }
  html, body {
    width: 1200px;
    height: 1200px;
    overflow: hidden;
    background: var(--board);
  }
  .board {
    position: relative;
    width: 1200px;
    height: 1200px;
    background: var(--board);
    font-family: "Questrial", sans-serif;
  }

  /* Label presentation panel */
  .label-stage {
    position: absolute;
    left: 0; top: 0;
    width: 740px; height: 867px;
    background: var(--stage);
  }
  .label {
    position: absolute;
    left: 91px; top: 35px;
    width: 554px; height: 824px;
  }
  .label__band {
    position: absolute;
    left: 0; width: 100%;
    background: var(--forest);
  }
  .label__band--top { top: 0; height: 55px; }
  .label__band--bottom { bottom: 0; height: 83px; }
  .label__paper {
    position: absolute;
    left: 0; top: 55px;
    width: 100%; height: 686px;
    background: radial-gradient(ellipse at 40% 40%, var(--label-paper) 0%, var(--mist) 60%, #D8D8D6 100%);
    text-align: center;
  }
  .label__mark {
    position: absolute;
    left: 50%; top: 33px;
    transform: translateX(-50%);
  }
  .label__brand {
    position: absolute;
    left: 0; width: 100%;
    top: 188px;
    font-family: "Josefin Sans", sans-serif;
    font-weight: 400;
    font-size: 40px;
    letter-spacing: 9px;
    color: var(--gold);
    padding-left: 9px;
  }
  .label__number {
    position: absolute;
    left: 0; width: 100%;
    top: 262px;
    font-family: "Permanent Marker", cursive;
    font-size: 150px;
    line-height: 1;
    color: var(--forest);
    letter-spacing: 4px;
  }
  .label__kind,
  .wordmark__kind {
    display: flex;
    align-items: center;
    justify-content: center;
    color: var(--ink-soft);
    text-transform: uppercase;
  }
  .label__kind {
    position: absolute;
    left: 100px; width: 354px;
    top: 456px;
    font-size: 25px;
    gap: 16px;
  }
  .label__kind::before,
  .label__kind::after,
  .wordmark__kind::before,
  .wordmark__kind::after {
    content: "";
    flex: 1;
    height: 2px;
    background: var(--forest);
  }
  .label__copy {
    position: absolute;
    left: 60px; width: 434px;
    top: 528px;
    color: var(--ink-soft);
  }
  .label__tagline {
    font-size: 21px;
    margin-bottom: 6px;
  }
  .label__body {
    font-size: 15.5px;
    line-height: 29px;
  }

  /* Serving scene placeholder */
  .serve-scene {
    position: absolute;
    left: 740px; top: 0;
    width: 460px; height: 867px;
    background: linear-gradient(180deg, #E4E4E8 0%, #D3D3D7 48%, #6B5A48 52%, #4E4136 100%);
  }

  /* Palette */
  .palette__swatch {
    position: absolute;
    top: 912px;
    width: 171px; height: 245px;
    font-size: 23px;
    padding: 0 0 24px 18px;
    display: flex;
    align-items: flex-end;
    font-family: "Questrial", sans-serif;
  }
  .palette__swatch--forest { left: 61px; background: var(--forest); color: var(--white); }
  .palette__swatch--gold   { left: 288px; background: var(--gold); color: var(--white); }
  .palette__swatch--mist   { left: 514px; background: var(--mist); color: var(--ink-soft); }

  /* Wordmark */
  .wordmark {
    position: absolute;
    left: 782px; top: 918px;
    width: 360px;
    text-align: center;
  }
  .wordmark__number {
    font-family: "Permanent Marker", cursive;
    font-size: 150px;
    line-height: 1;
    color: var(--forest);
    letter-spacing: 4px;
  }
  .wordmark__kind {
    margin-top: 42px;
    font-size: 26px;
    gap: 18px;
  }
</style>
</head>
<body>
<main class="board">

  <section class="label-stage">
    <div class="label">
      <div class="label__band label__band--top"></div>
      <div class="label__paper">
        <svg class="label__mark" width="108" height="108" viewBox="0 0 108 108" aria-hidden="true">
          <circle cx="54" cy="54" r="50" fill="none" stroke="var(--gold)" stroke-width="4"/>
        </svg>
        <div class="label__brand">VELMO</div>
        <div class="label__number">1764</div>
        <div class="label__kind">Reed Whisky</div>
        <div class="label__copy">
          <p class="label__tagline">Tristique nulla aliquet enim tortor</p>
          <p class="label__body">Lorem ipsum dolor sit amet, consectetur adipiscing elit, sed do eiusmod tempor incididunt ut labore et dolore magna aliqua. Leo vel orci porta non.</p>
        </div>
      </div>
      <div class="label__band label__band--bottom"></div>
    </div>
  </section>

  <div class="serve-scene" role="img" aria-label="Photograph of the labelled amber whisky bottle beside a glass of whisky on ice on a wooden table"></div>

  <section class="palette">
    <div class="palette__swatch palette__swatch--forest">#13322B</div>
    <div class="palette__swatch palette__swatch--gold">#B38808</div>
    <div class="palette__swatch palette__swatch--mist">#E1E0DC</div>
  </section>

  <section class="wordmark">
    <div class="wordmark__number">1764</div>
    <div class="wordmark__kind">Reed Whisky</div>
  </section>

</main>
</body>
</html>
```